Bref créative
Business card design for
Keep-N-Cozy Self Storage, LLC
Simple
Dale Vinter
Manager
2870 Marlow Rd.
dvinter@mailquay.net
Bins-Ready-Now.net
The business card design should incorportate the logo from the logo project.

```html
<!DOCTYPE html>
<html lang="en">
<head>
<meta charset="utf-8">
<title>Keep-N-Cozy Self Storage — Stationery</title>
<link rel="stylesheet" href="https://fonts.googleapis.com/css2?family=Open+Sans:wght@400;700&display=swap">
<style>
:root{
  --bg:#e9e6e1;
  --paper:#ffffff;
  --green:#1f5a34;
  --green-dark:#153f24;
  --gold:#b39a52;
  --ink:#3b3b3b;
  --muted:#8a8a8a;
}
*{box-sizing:border-box;margin:0;padding:0}
html,body{width:1200px;height:341px;overflow:hidden}
body{background:var(--bg);font-family:"Open Sans",Arial,sans-serif;color:var(--ink);position:relative}
.sheet{position:absolute;background:var(--paper);box-shadow:0 2px 5px rgba(0,0,0,.25);overflow:hidden}
.swoosh{position:absolute;inset:0;width:100%;height:100%}
.brand{position:absolute;display:flex;align-items:center;gap:3px;color:var(--green);font-weight:700;line-height:1;white-space:nowrap}
.brand-square{background:var(--green);display:block}
.card{width:182px;height:66px;left:34px}
.card--front{top:144px}
.card--back{top:235px}
.card .brand{left:10px;top:9px;font-size:9px}
.card .brand-square{width:8px;height:8px}
.card-person{position:absolute;left:62px;top:22px;font-size:5px;line-height:1.35}
.card-person .name{font-weight:700;font-size:6px;color:var(--green)}
.card-contact{position:absolute;left:128px;top:10px;font-size:4px;line-height:1.5;color:var(--muted);white-space:nowrap}
.letterhead{width:144px;height:288px;top:29px}
.letterhead--one{left:240px}
.letterhead--two{left:408px}
.letterhead .brand{left:22px;top:14px;font-size:8px}
.letterhead .brand-square{width:7px;height:7px}
.letterhead-contact{position:absolute;left:98px;top:13px;font-size:3.5px;line-height:1.6;color:var(--muted);white-space:nowrap}
.letterhead-footer{position:absolute;left:0;right:0;bottom:14px;text-align:center;font-size:3.5px;color:var(--muted)}
.envelope{width:209px;height:91px;left:643px}
.envelope--one{top:96px}
.envelope--two{top:204px}
.envelope .brand{left:10px;top:9px;font-size:8px}
.envelope .brand-square{width:7px;height:7px}
.envelope-return{position:absolute;left:22px;top:22px;font-size:3.5px;line-height:1.5;color:var(--muted)}
.flap{width:233px;height:80px;left:907px}
.flap--gold{top:48px}
.flap--green{top:140px}
.flap--front{top:232px}
.flap .brand{left:50%;transform:translate(-50%,-50%);font-size:8px}
.flap .brand-square{width:7px;height:7px}
</style>
</head>
<body>

<section class="sheet card card--front">
  <svg class="swoosh" viewBox="0 0 182 66" preserveAspectRatio="none" aria-hidden="true">
    <path d="M0 44 Q10 60 40 66 L0 66Z" fill="var(--green)"/>
    <path d="M150 0 Q176 6 182 28 L182 0Z" fill="var(--green)"/>
  </svg>
  <div class="brand"><span class="brand-square"></span>Keep-N-Cozy</div>
  <div class="card-person">
    <div class="name">Dale Vinter</div>
    <div>Manager</div>
  </div>
  <div class="card-contact">
    <div>Phone 555-0142</div>
    <div>2870 Marlow Rd.</div>
    <div>dvinter@mailquay.net</div>
    <div>Bins-Ready-Now.net</div>
  </div>
</section>

<section class="sheet card card--back">
  <svg class="swoosh" viewBox="0 0 182 66" preserveAspectRatio="none" aria-hidden="true">
    <path d="M0 0 L60 0 Q20 20 0 50Z" fill="var(--green)"/>
    <path d="M182 30 Q170 60 130 66 L182 66Z" fill="var(--green)"/>
  </svg>
  <div class="card-person" style="left:70px;top:14px">
    <div class="name">Dale Vinter</div>
    <div>Manager</div>
    <div>Phone 555-0142</div>
    <div>dvinter@mailquay.net</div>
    <div>Bins-Ready-Now.net</div>
  </div>
</section>

<section class="sheet letterhead letterhead--one">
  <svg class="swoosh" viewBox="0 0 144 288" preserveAspectRatio="none" aria-hidden="true">
    <path d="M0 0 L30 0 Q8 14 0 36Z" fill="var(--green)"/>
    <path d="M144 250 Q138 280 110 288 L144 288Z" fill="var(--green)"/>
  </svg>
  <div class="brand"><span class="brand-square"></span>Keep-N-Cozy</div>
  <div class="letterhead-contact">
    <div>2870 Marlow Rd.</div>
    <div>Phone 555-0142</div>
    <div>Bins-Ready-Now.net</div>
  </div>
</section>

<section class="sheet letterhead letterhead--two">
  <svg class="swoosh" viewBox="0 0 144 288" preserveAspectRatio="none" aria-hidden="true">
    <path d="M0 0 L30 0 Q8 14 0 36Z" fill="var(--green)"/>
    <path d="M144 250 Q138 280 110 288 L144 288Z" fill="var(--green)"/>
  </svg>
  <div class="brand"><span class="brand-square"></span>Keep-N-Cozy</div>
  <div class="letterhead-footer">2870 Marlow Rd. · dvinter@mailquay.net · Bins-Ready-Now.net</div>
</section>

<section class="sheet envelope envelope--one">
  <svg class="swoosh" viewBox="0 0 209 91" preserveAspectRatio="none" aria-hidden="true">
    <path d="M0 62 Q8 84 34 91 L0 91Z" fill="var(--green)"/>
  </svg>
  <div class="brand"><span class="brand-square"></span>Keep-N-Cozy</div>
  <div class="envelope-return"><div>2870 Marlow Rd.</div><div>Bins-Ready-Now.net</div></div>
</section>

<section class="sheet envelope envelope--two">
  <svg class="swoosh" viewBox="0 0 209 91" preserveAspectRatio="none" aria-hidden="true">
    <path d="M0 62 Q8 84 34 91 L0 91Z" fill="var(--green)"/>
  </svg>
  <div class="brand"><span class="brand-square"></span>Keep-N-Cozy</div>
  <div class="envelope-return"><div>2870 Marlow Rd.</div><div>Bins-Ready-Now.net</div></div>
</section>

<section class="sheet flap flap--gold">
  <svg class="swoosh" viewBox="0 0 233 80" preserveAspectRatio="none" aria-hidden="true">
    <path d="M0 0 L233 0 L233 12 L116 58 L0 12Z" fill="var(--gold)"/>
    <path d="M0 0 L233 0 L233 6 L116 50 L0 6Z" fill="var(--green)"/>
  </svg>
  <div class="brand" style="top:74%"><span class="brand-square"></span>Keep-N-Cozy</div>
</section>

<section class="sheet flap flap--green">
  <svg class="swoosh" viewBox="0 0 233 80" preserveAspectRatio="none" aria-hidden="true">
    <path d="M0 0 L233 0 L233 10 L116 52 L0 10Z" fill="var(--green)"/>
  </svg>
  <div class="brand" style="top:76%"><span class="brand-square"></span>Keep-N-Cozy</div>
</section>

<section class="sheet flap flap--front">
  <svg class="swoosh" viewBox="0 0 233 80" preserveAspectRatio="none" aria-hidden="true">
    <path d="M0 0 L233 0 L116 44Z" fill="none" stroke="#cfcfcf" stroke-width="1"/>
    <path d="M0 56 Q6 74 28 80 L0 80Z" fill="var(--green)"/>
  </svg>
</section>

</body>
</html>
```